Coral Ridge Roofing LLC introduction postcard design

I am looking to get designs for post cards I will be sending out to Homeowners, contractors and Management companies introducing our services, this card will be one sided an area to add a mailing sticker the card will be 4.2x5.5 inches you can get some ideas from www.coralridgeroofing-example.com

```html
<!DOCTYPE html>
<html lang="en">
<head>
<meta charset="utf-8">
<title>Coral Ridge Roofing LLC – Introduction Postcard</title>
<link rel="stylesheet" href="https://fonts.googleapis.com/css2?family=Oswald:wght@700&family=Rubik:wght@400;500;600&display=swap">
<style>
:root{
  --bg:#e9e9ea;
  --blue:#2f74ad;
  --blue-dark:#245f91;
  --yellow:#fbbd3b;
  --navy:#1c2d4f;
  --service:#1f4f86;
  --white:#ffffff;
  --line:#d9d9d9;
  --stamp:#ededee;
}
*{margin:0;padding:0;box-sizing:border-box}
html,body{width:1200px;height:3121px;overflow:hidden;background:var(--bg)}
body{position:relative;font-family:'Rubik',Arial,sans-serif}
.card{position:absolute;left:189px;width:822px;height:628px;background:var(--white);overflow:hidden}
.card--front{top:963px}
.card--back{top:1646px}
.abs{position:absolute}

/* front */
.photo-strip{left:0;top:0;width:30px;height:354px;background:linear-gradient(180deg,#7fa7c9 0%,#8c9aa3 60%,#6d7a86 100%)}
.headline-panel{left:30px;top:0;width:366px;height:354px;background:var(--blue)}
.hero-photo{left:396px;top:0;width:426px;height:354px;background:linear-gradient(170deg,#5d95cf 0%,#b9d3ea 40%,#8f9aa5 70%,#5e6b78 100%)}
.services-panel{left:30px;top:293px;width:366px;height:335px;background:var(--yellow)}
.headline{left:63px;top:26px;font-family:'Oswald',Impact,sans-serif;font-weight:700;font-size:52px;line-height:54px;color:var(--white);text-transform:uppercase;letter-spacing:-.5px;white-space:nowrap;transform:scale(.81,1.03);transform-origin:top left}
.headline .accent{color:var(--yellow)}
.tagline{left:63px;top:258px;font-size:18px;font-weight:500;color:var(--white)}
.services-bar{left:39px;top:305px;width:282px;height:40px;background:var(--blue)}
.services-bar span{position:absolute;left:20px;top:7px;font-size:22px;font-weight:500;color:var(--white);letter-spacing:.3px}
.slashes{left:278px;top:302px}
.services-list{left:56px;top:352px;list-style:none}
.services-list li{display:flex;align-items:center;height:31.5px;font-size:20.5px;font-weight:500;color:var(--service);white-space:nowrap}
.services-list svg{margin-right:14px;flex:none}
.brand{display:flex;align-items:center;gap:10px}
.brand-mark{width:34px;height:34px;border-radius:50%;background:var(--navy);flex:none}
.brand-name{font-size:22px;font-weight:600;color:var(--navy)}
.brand--front{left:476px;top:378px}
.cta{background:var(--yellow);color:var(--white);font-weight:500;border-radius:4px;text-align:center;text-transform:uppercase}
.cta--front{left:434px;top:474px;width:213px;height:34px;font-size:18px;line-height:34px}
.contacts{list-style:none}
.contacts li{display:flex;align-items:center;font-weight:500;color:var(--navy);white-space:nowrap}
.contacts svg{flex:none}
.contacts--front{left:434px;top:514px}
.contacts--front li{height:30.5px;font-size:16px}
.contacts--front svg{margin-right:13px}

/* back */
.info-panel{left:23px;top:0;width:423px;height:499px;background:var(--blue);border-bottom:4px solid var(--yellow)}
.info-title{left:58px;top:30px;font-size:24px;font-weight:500;color:var(--white)}
.info-text{left:58px;top:64px;width:361px;font-size:12.4px;line-height:15.8px;color:#e8f0f8;text-align:justify}
.divider{left:58px;top:195px;width:361px;height:2px;background:var(--yellow)}
.info-heading{font-size:19.5px;font-weight:500;color:var(--white);white-space:nowrap}
.info-heading--1{left:58px;top:215px}
.info-heading--2{left:54px;top:348px}
.ticks{list-style:none;color:#e8f0f8;font-size:12.5px}
.ticks li{position:absolute;display:flex;align-items:center;white-space:nowrap}
.ticks svg{margin-right:10px;flex:none}
.choose-text{left:54px;top:381px;width:370px;font-size:11.2px;line-height:13.6px;color:#e8f0f8}
.ticks--choose li{font-size:11.5px;line-height:12px;font-weight:500}
.cta--back{left:143px;top:485px;width:179px;height:27px;font-size:15px;line-height:27px}
.contacts--back{left:40px;top:526px}
.contacts--back li{height:30px;font-size:21.5px}
.contacts--back svg{margin-right:16px}
.brand--back{left:485px;top:46px;gap:10px}
.brand--back .brand-mark{width:30px;height:30px}
.brand--back .brand-name{font-size:15px;line-height:18px}
.licence{left:481px;top:140px;font-size:10px;color:var(--navy)}
.mail-address{left:481px;top:163px;font-size:12.6px;line-height:16px;font-weight:600;color:var(--navy)}
.stamp{left:703px;top:55px;width:73px;height:72px;background:var(--stamp)}
.address-line{left:490px;width:327px;height:2px;background:var(--line)}
</style>
</head>
<body>
<svg width="0" height="0" style="position:absolute" aria-hidden="true">
  <defs>
    <symbol id="tick-light" viewBox="0 0 16 16"><circle cx="8" cy="8" r="7.5" fill="#ffffff" fill-opacity=".85"/><path d="M4.6 8.2l2.3 2.3 4.5-4.7" fill="none" stroke="#fbbd3b" stroke-width="1.8" stroke-linecap="round" stroke-linejoin="round"/></symbol>
    <symbol id="icon-phone" viewBox="0 0 20 20"><path d="M5 2.5l3 3.2-1.6 2a10 10 0 004.9 4.9l2-1.6 3.2 3-1.7 2.7C9.5 17 3 10.5 2.3 4.2z" fill="none" stroke="#fbbd3b" stroke-width="1.6" stroke-linejoin="round"/><path d="M12 2.5a5.5 5.5 0 015.5 5.5M12 5.5A2.5 2.5 0 0114.5 8" fill="none" stroke="#fbbd3b" stroke-width="1.4" stroke-linecap="round"/></symbol>
    <symbol id="icon-mail" viewBox="0 0 20 20"><rect x="2" y="5" width="16" height="12" rx="1.5" fill="none" stroke="#fbbd3b" stroke-width="1.6"/><path d="M2.5 6l7.5 6 7.5-6" fill="none" stroke="#fbbd3b" stroke-width="1.6" stroke-linejoin="round"/></symbol>
    <symbol id="icon-globe" viewBox="0 0 20 20"><circle cx="10" cy="10" r="7.6" fill="none" stroke="#fbbd3b" stroke-width="1.5"/><ellipse cx="10" cy="10" rx="3.4" ry="7.6" fill="none" stroke="#fbbd3b" stroke-width="1.3"/><path d="M2.6 10h14.8M4 6h12M4 14h12" fill="none" stroke="#fbbd3b" stroke-width="1.2"/></symbol>
  </defs>
</svg>

<section class="card card--front" aria-label="Postcard front">
  <div class="abs photo-strip" role="img" aria-label="Photo edge of a house roof under blue sky"></div>
  <div class="abs headline-panel"></div>
  <div class="abs hero-photo" role="img" aria-label="Photo of a roofer in hard hat fitting metal tile roofing under a cloudy blue sky"></div>
  <div class="abs services-panel"></div>

  <h1 class="abs headline">Your Trusted<br>Roofing Experts<br><span class="accent">In Vero Beach,<br>Florida</span></h1>
  <p class="abs tagline">Built for the Coast, Built for You.</p>

  <div class="abs services-bar"><span>OUR SERVICES</span></div>
  <svg class="abs slashes" width="44" height="46" viewBox="0 0 44 46" aria-hidden="true"><path d="M14 2h9L11 44H2zM32 2h9L29 44h-9z" fill="#ffffff"/></svg>

  <ul class="abs services-list">
    <li><svg width="17" height="17"><use href="#tick-light"/></svg>Roof Replacement</li>
    <li><svg width="17" height="17"><use href="#tick-light"/></svg>Roof Repairs</li>
    <li><svg width="17" height="17"><use href="#tick-light"/></svg>Roof Inspection</li>
    <li><svg width="17" height="17"><use href="#tick-light"/></svg>Storm Damage Services</li>
    <li><svg width="17" height="17"><use href="#tick-light"/></svg>Emergency Services</li>
    <li><svg width="17" height="17"><use href="#tick-light"/></svg>Roof Maintenance Program</li>
    <li><svg width="17" height="17"><use href="#tick-light"/></svg>Commercial Roofing</li>
    <li><svg width="17" height="17"><use href="#tick-light"/></svg>Roof Tune-Up Services</li>
  </ul>

  <div class="abs brand brand--front"><span class="brand-mark"></span><span class="brand-name">Coral Ridge Roofing LLC</span></div>

  <div class="abs cta cta--front">Get in touch now</div>
  <ul class="abs contacts contacts--front">
    <li><svg width="18" height="18"><use href="#icon-phone"/></svg>(555) 014-8826</li>
    <li><svg width="18" height="18"><use href="#icon-mail"/></svg>quick.help@coralridgeroofing-example.com</li>
    <li><svg width="18" height="18"><use href="#icon-globe"/></svg>www.coralridgeroofing-example.com</li>
  </ul>
</section>

<section class="card card--back" aria-label="Postcard back">
  <div class="abs info-panel"></div>
  <h2 class="abs info-title">Expert Roof Repair Vero Beach</h2>
  <p class="abs info-text">A roof is the most important part of a house because it shields the home from environmental factors, whether it is an extreme temperature, heavy rainfall, or a cyclone. So, why not keep the roof in its best shape? Search for the best roof repair Vero Beach on the internet, and you will easily find experts for this task. We are Coral Ridge Roofing LLC, serving homeowners with quality roof repair services at budget-friendly costs.</p>
  <div class="abs divider"></div>

  <h3 class="abs info-heading info-heading--1">Why is Roof Repair Important?</h3>
  <ul class="ticks">
    <li style="left:59px;top:251px"><svg width="14" height="14"><use href="#tick-light"/></svg>Protects the Interior</li>
    <li style="left:59px;top:275px"><svg width="14" height="14"><use href="#tick-light"/></svg>Extends Roof Lifespan</li>
    <li style="left:59px;top:300px"><svg width="14" height="14"><use href="#tick-light"/></svg>It is More Cost Effective</li>
    <li style="left:235px;top:253px"><svg width="14" height="14"><use href="#tick-light"/></svg>Increases Property Value</li>
    <li style="left:235px;top:277px"><svg width="14" height="14"><use href="#tick-light"/></svg>Improves Safety</li>
  </ul>

  <h3 class="abs info-heading info-heading--2">Why Choose Us for Roofing Services?</h3>
  <p class="abs choose-text">Those searching for roofing repair contractors Vero Beach can select us. We are the top choice for roofing services, thanks to our quality services and ability to deliver great customer experiences.</p>
  <ul class="ticks ticks--choose">
    <li style="left:56px;top:440px"><svg width="14" height="14"><use href="#tick-light"/></svg>Fully Licensed<br>and Insured</li>
    <li style="left:171px;top:440px"><svg width="14" height="14"><use href="#tick-light"/></svg>Experts in<br>Roofing Services</li>
    <li style="left:307px;top:434px"><svg width="14" height="14"><use href="#tick-light"/></svg>Fast, Reliable,<br>and Transparent<br>Services</li>
  </ul>

  <div class="abs cta cta--back">Get in touch now</div>
  <ul class="abs contacts contacts--back">
    <li><svg width="20" height="20"><use href="#icon-phone"/></svg>(555) 014-8826</li>
    <li><svg width="20" height="20"><use href="#icon-mail"/></svg>quick.help@coralridgeroofing-example.com</li>
    <li><svg width="20" height="20"><use href="#icon-globe"/></svg>www.coralridgeroofing-example.com</li>
  </ul>

  <div class="abs brand brand--back"><span class="brand-mark"></span><span class="brand-name">Coral Ridge<br>Roofing LLC</span></div>
  <p class="abs licence">Licence# CCC0000417</p>
  <p class="abs mail-address">418 Harbor Pine Rd,<br>Vero Beach FL 32960</p>
  <div class="abs stamp" aria-label="Stamp area"></div>
  <div class="abs address-line" style="top:305px"></div>
  <div class="abs address-line" style="top:351px"></div>
  <div class="abs address-line" style="top:398px"></div>
  <div class="abs address-line" style="top:445px"></div>
</section>
</body>
</html>
```